Tamarind Sailing needs a flyer promoting sailing holidays on the Coral Horizon Shoals

Tamarind Sailing is a private yacht charter company based in Sydney run by Mark & Jenny Dunford. We love sailing and our business allows us to share this passion with others. In winter 2015 (June - October) we're heading to Queensland, Australia to explore the Coral Horizon Shoals. We're offering sailing holidays on a large luxury yacht to small groups (max six guests on board, ideally four). We would like the design to complement our website (www.tamarindsailing.com.au) and reflect our tagline "where sailing meets fun and relaxation". I have attached a design brief with more information, some photos of previous trips to QLD and two versions of our logo.

Target Market(s)

Target markets are
-Small families (kid friendly) or couples with an interest in sailing or potential interest in sailing or
- Individuals who are learning to sail or love sailing or adventure travellers

Age bracket for both groups is 30-50.

Small families/couples will be professionals with well-paid jobs where they need a holiday where most things are done for them to wind down. They have a sense of adventure and would be bored just sitting on the beach. They like healthy living, fresh food and exercise, especially water sports (ideally sailing)

Individuals most likely will be learning to sail or adventure travellers looking for a different way to spend a few days away. They will earn a good wage in middle management, most likely come from the corporate world.

Industry/Entity Type

Business

Font styles to use
Sans Serif

Colors
0355a3
fece3f

Requirements
Must have
• Our Logo, contact details - name, email, website and phone no.
• Our Tagline.
Nice to have
• Wander Review logo, Chatterbook reference

```html
<!DOCTYPE html>
<html lang="en">
<head>
<meta charset="utf-8">
<title>Tamarind Sailing – Sailing Holidays Flyer</title>
<link href="https://fonts.googleapis.com/css2?family=Roboto+Condensed:wght@400;700&display=swap" rel="stylesheet">
<style>
  :root {
    --navy: #0b2b50;
    --navy-deep: #081f3b;
    --brand-blue: #0355a3;
    --yellow: #fece3f;
    --white: #ffffff;
    --sand: #e9dcc0;
    --sea: #5fb3cf;
    --sky: #a9d3e8;
  }
  html, body {
    margin: 0;
    padding: 0;
    width: 1200px;
    height: 2514px;
    overflow: hidden;
    background: var(--navy);
  }
  .flyer {
    position: relative;
    width: 1200px;
    height: 2514px;
    background: var(--navy);
    font-family: "Roboto Condensed", "Arial Narrow", sans-serif;
    color: var(--white);
    overflow: hidden;
  }

  /* Intro section */
  .intro {
    position: relative;
    height: 880px;
    box-sizing: border-box;
    padding: 30px 60px 0 80px;
  }
  .intro-photo {
    position: absolute;
    top: 0;
    right: 0;
    width: 600px;
    height: 500px;
    background:
      linear-gradient(to bottom, rgba(11,43,80,0) 55%, var(--navy) 100%),
      linear-gradient(to left, rgba(11,43,80,0) 70%, var(--navy) 100%),
      linear-gradient(to bottom, var(--sky) 0%, #cfe4ee 35%, var(--sea) 50%, var(--sand) 72%, #c9b48d 100%);
  }
  .intro-content { position: relative; }
  .intro-spacer {
    float: right;
    width: 470px;
    height: 440px;
  }
  .tagline {
    margin: 0 0 16px;
    font-size: 54px;
    line-height: 1.08;
    font-weight: 700;
    color: var(--yellow);
  }
  .intro-text {
    margin: 0;
    font-size: 35px;
    line-height: 1.42;
    font-weight: 400;
  }
  .intro-text.highlight { color: var(--yellow); }

  /* Photo strip */
  .photo-strip {
    display: flex;
    gap: 6px;
    height: 250px;
    background: var(--white);
  }
  .strip-photo { flex: 1; }
  .strip-photo.jetty {
    background: linear-gradient(to bottom, #9ccbe2 0%, #bfe0ec 45%, #3f9ec4 55%, #2a7ea5 100%);
  }
  .strip-photo.beach {
    background: linear-gradient(to bottom, #7fb7d6 0%, #b6d8e6 40%, #4ba7c8 52%, #e3d6b5 78%, #d3c29b 100%);
  }
  .strip-photo.hammock {
    background: linear-gradient(to bottom, #8fc3df 0%, #cde4ee 45%, #3d98c0 60%, #2c6f8f 100%);
  }

  /* Departures */
  .departures {
    box-sizing: border-box;
    padding: 80px 60px 0;
    text-align: center;
  }
  .departures p {
    margin: 0;
    font-size: 38px;
    line-height: 1.5;
  }
  .season {
    margin: 6px 0 4px;
    font-size: 72px;
    line-height: 1.1;
    font-weight: 700;
    color: var(--yellow);
  }
  .season.late { margin-top: 16px; }

  /* Contact band */
  .contact-band {
    position: absolute;
    top: 2100px;
    left: 0;
    width: 1200px;
    height: 320px;
    background: var(--white);
    color: var(--navy);
  }
  .brand-mark {
    position: absolute;
    left: 80px;
    top: 70px;
    width: 300px;
    text-align: center;
  }
  .brand-dot {
    display: block;
    width: 96px;
    height: 96px;
    margin: 0 auto 18px;
    border-radius: 50%;
    background: var(--brand-blue);
  }
  .brand-name {
    font-size: 44px;
    font-weight: 700;
    color: var(--navy);
    line-height: 1.05;
    text-transform: uppercase;
    letter-spacing: 2px;
  }
  .contact-list {
    position: absolute;
    left: 655px;
    top: 40px;
    margin: 0;
    padding: 0;
    list-style: none;
  }
  .contact-list li {
    display: flex;
    align-items: center;
    gap: 22px;
    font-size: 36px;
    line-height: 52px;
    color: var(--navy);
  }
  .contact-list svg { width: 28px; height: 28px; flex: none; }
  .listings {
    position: absolute;
    left: 655px;
    top: 222px;
    display: flex;
    align-items: center;
    gap: 40px;
    font-size: 30px;
    font-weight: 700;
    color: var(--navy);
  }
  .listing { display: flex; align-items: center; gap: 14px; }
  .listing-square {
    width: 34px;
    height: 34px;
    background: var(--brand-blue);
  }
  .listing-circle {
    width: 48px;
    height: 48px;
    border-radius: 50%;
    background: var(--navy);
  }

  /* Footer */
  .site-footer {
    position: absolute;
    top: 2420px;
    left: 0;
    width: 1200px;
    height: 94px;
    background: var(--navy-deep);
    text-align: center;
    font-size: 42px;
    line-height: 94px;
  }
</style>
</head>
<body>
<main class="flyer">

  <section class="intro">
    <div class="intro-photo" role="img" aria-label="Photo of a tropical beach with a palm and hammock beside turquoise water"></div>
    <div class="intro-content">
      <div class="intro-spacer"></div>
      <h1 class="tagline">Where sailing meets fun and relaxation</h1>
      <p class="intro-text">Sailing holidays/mini-breaks on the Coral Horizon Shoals. Skippered sailing charters on board a beautiful 58 foot sailing yacht. Maximum six guests on board a fully crewed 58-foot yacht (most other yachts offering this service are smaller and usually have 10-12 guests on board).</p>
      <p class="intro-text highlight">Minimum stay is 2 nights/3 days, with additional nights available.</p>
      <p class="intro-text">Activities include sailing, snorkelling, bush-walking, paddle-boarding, whale-watching, fishing and relaxing in the hammock No sailing knowledge required and sailing lessons can be incorporated into the holiday.</p>
      <p class="intro-text highlight">Flexible itinerary to meet guests' requirements.</p>
      <p class="intro-text">Fully catered with fresh healthy seasonal dishes. Drinks package available on request and highly recommended for sun-downers!</p>
    </div>
  </section>

  <section class="photo-strip">
    <div class="strip-photo jetty" role="img" aria-label="Photo of a wooden jetty reaching into calm blue water"></div>
    <div class="strip-photo beach" role="img" aria-label="Photo of a sandy island beach with deck chairs"></div>
    <div class="strip-photo hammock" role="img" aria-label="Photo of a hammock strung between palms over the sea"></div>
  </section>

  <section class="departures">
    <p>Pick up is on Fridays and flexible departure and<br>arrival options as follows:</p>
    <h2 class="season">June - July</h2>
    <p>Townsville to explore Magnetic Island and beyond Or Airlie<br>Beach, Shute Harbour or Hamilton<br>Island to explore the Whitsundays and beyond</p>
    <h2 class="season late">September - October</h2>
    <p>Mackay or Rockhampton to explore the reefs and islands in the<br>surrounding area</p>
  </section>

  <section class="contact-band">
    <div class="brand-mark">
      <span class="brand-dot"></span>
      <div class="brand-name">Tamarind<br>Sailing</div>
    </div>
    <ul class="contact-list">
      <li>
        <svg viewBox="0 0 24 24" aria-hidden="true"><path fill="#0b2b50" d="M6.6 10.8a15.1 15.1 0 0 0 6.6 6.6l2.2-2.2a1 1 0 0 1 1-.25 11.4 11.4 0 0 0 3.6.57 1 1 0 0 1 1 1V20a1 1 0 0 1-1 1A17 17 0 0 1 3 4a1 1 0 0 1 1-1h3.5a1 1 0 0 1 1 1c0 1.250.2 2.450.57 3.57a1 1 0 0 1-.25 1z"/></svg>
        0491 570 338
      </li>
      <li>
        <svg viewBox="0 0 24 24" aria-hidden="true"><path fill="#0b2b50" d="M6.6 10.8a15.1 15.1 0 0 0 6.6 6.6l2.2-2.2a1 1 0 0 1 1-.25 11.4 11.4 0 0 0 3.6.57 1 1 0 0 1 1 1V20a1 1 0 0 1-1 1A17 17 0 0 1 3 4a1 1 0 0 1 1-1h3.5a1 1 0 0 1 1 1c0 1.250.2 2.450.57 3.57a1 1 0 0 1-.25 1z"/></svg>
        0487 213 654
      </li>
      <li>
        <svg viewBox="0 0 24 24" aria-hidden="true"><rect x="2" y="5" width="20" height="14" rx="1" fill="#0b2b50"/><path d="M3 6l9 7 9-7" fill="none" stroke="#ffffff" stroke-width="1.6"/></svg>
        info@tamarindsailing.com.au
      </li>
    </ul>
    <div class="listings">
      <div class="listing"><span class="listing-square"></span>Chatterbook</div>
      <div class="listing"><span class="listing-circle"></span>Wander Review</div>
    </div>
  </section>

  <footer class="site-footer">www.tamarindsailing.com.au</footer>

</main>
</body>
</html>
```